Verpackungsdesign für Wellness- und Saunaprodukte
Zielgruppe
Brisavo ist ein junges Start-Up, das sich auf Wellness- und Saunaprodukte spezialisiert hat. Unsere Zielgruppe besteht zu beinahe gleichen Teilen aus männlichen und weiblichen Personen zwischen 30 und 60 Jahren. Unsere Produkte befinden sich eher im mittel- bis höherpreisigen Segment, daher streben wir ein hochwertiges Design für unsere Verpackungen an. Unsere Produktpalette reicht von Mentholkristallen, Saunaaufgüssen, bis hin zu Textilien für den Wellnessbereich und soll dementsprechend Menschen ansprechen, die sich einen gewissen Luxus im Alltag auch gönnen.
Aufgabenstellung
Inspiriert von der skandinavischen Sauna Kultur, möchten wir Momente der Erholung und
Entspannung in den Alltag unserer Kunden bringen. Die Geschichte des Saunierens ist eng mit der skandinavischen Kultur verbunden und skandinavische Stilelemente sind zeitgemäß und sprechen ein breites Publikum an. Das Design muss auf Dosen/Tiegel , Karton Verpackungen und Flaschen verschiedener Größen adaptierbar sein (siehe Bild im Anhang).
40g Tiegel(transparent) Höhe 40mm Durchmesser 60mm (ohne Deckel Silber gebürstet)
100g Tiegel(transparent) Höhe 53mm Durchmesser 71mm (ohne Deckel Silber gebürstet)
200g Tiegel(transparent) Höhe 65mm Durchmesser 90mm (ohne Deckel Silber gebürstet)
Karton Verpackung 124,5x49x49mm
Karton Verpackung 100x100x100mm
Flaschenetikett 134x67mm (Braunglas, schwarzer Deckel)
Es soll ein passendes Keyvisual erstellt werden.
Im Anhang sieht man die Verpackungen, Dosen, Flaschen sowie unsere ersten Design Entwürfe (an diese Anordnung der Elemente kann sich der Designer orientieren ). Das Logo bleibt wie gegeben. Das Produkt für die Tiegel soll Mentholkristalle sein.

```html
<!DOCTYPE html>
<html lang="de">
<head>
<meta charset="UTF-8">
<title>Brisavo – Flaschenetiketten</title>
<link href="https://fonts.googleapis.com/css2?family=Fira+Sans:wght@400;700&family=Dancing+Script:wght@500&display=swap" rel="stylesheet">
<style>
  :root {
    --canvas: #ffffff;
    --label-paper: #f4f3f1;
    --label-edge: #e2e0dc;
    --brand-ink: #6b6b6b;
    --title-ink: #ffffff;
    --fichte-band: #b8ccb3;
    --fichte-ink: #2e4a3b;
    --fichte-art: #6f8a78;
    --menthol-band: #cfe2ea;
    --menthol-ink: #2a6f80;
    --menthol-art: #7fb0bd;
    --granat-band: #e6a3a4;
    --granat-ink: #a6485a;
    --granat-art: #c98c96;
  }
  * { box-sizing: border-box; margin: 0; padding: 0; }
  html, body {
    width: 1200px;
    height: 848px;
    overflow: hidden;
    background: var(--canvas);
  }
  .canvas {
    position: relative;
    width: 1200px;
    height: 848px;
    display: flex;
    justify-content: center;
    align-items: center;
    gap: 90px;
  }
  .label {
    position: relative;
    width: 200px;
    height: 400px;
    background: var(--label-paper);
    border: 1px solid var(--label-edge);
    overflow: hidden;
  }
  .label__brand {
    position: absolute;
    top: 0;
    left: 0;
    right: 0;
    height: 97px;
    display: flex;
    flex-direction: column;
    align-items: center;
    justify-content: center;
    gap: 6px;
  }
  .brand-mark {
    width: 14px;
    height: 14px;
    border: 1.5px solid var(--brand-ink);
    border-radius: 50%;
  }
  .brand-name {
    font-family: "Fira Sans", sans-serif;
    font-weight: 400;
    font-size: 12px;
    letter-spacing: 0.3px;
    color: var(--brand-ink);
  }
  .label__band {
    position: absolute;
    top: 97px;
    left: 0;
    right: 0;
    height: 200px;
    text-align: center;
    padding-top: 36px;
  }
  .label__title {
    font-family: "Fira Sans", sans-serif;
    font-weight: 700;
    font-size: 30px;
    line-height: 36px;
    letter-spacing: 0.5px;
    color: var(--title-ink);
    text-transform: uppercase;
  }
  .label__title--wide { font-size: 28px; letter-spacing: 0; }
  .label__tagline {
    margin-top: 12px;
    font-family: "Dancing Script", cursive;
    font-weight: 500;
    font-size: 16px;
  }
  .label__art {
    position: absolute;
    left: 0;
    right: 0;
    bottom: 8px;
    height: 130px;
  }
  .label__art--fichte { left: 30px; right: 6px; }
  .label__art--menthol { left: 0; right: 20px; }
  .label__art--granat { left: 10px; right: 20px; }

  .label--fichte .label__band { background: var(--fichte-band); }
  .label--fichte .label__tagline { color: var(--fichte-ink); }
  .label--fichte .label__art {
    background: linear-gradient(180deg, rgba(111,138,120,0) 0%, var(--fichte-art) 100%);
    opacity: 0.7;
  }
  .label--menthol .label__band { background: var(--menthol-band); }
  .label--menthol .label__tagline { color: var(--menthol-ink); }
  .label--menthol .label__art {
    background: radial-gradient(ellipse at 50% 60%, var(--menthol-art) 0%, rgba(127,176,189,0) 70%);
    opacity: 0.8;
  }
  .label--granat .label__band { background: var(--granat-band); }
  .label--granat .label__tagline { color: var(--granat-ink); }
  .label--granat .label__art {
    background: radial-gradient(ellipse at 50% 60%, var(--granat-art) 0%, rgba(201,140,150,0) 70%);
    opacity: 0.8;
  }
</style>
</head>
<body>
<main class="canvas">

  <section class="label label--fichte">
    <header class="label__brand">
      <span class="brand-mark"></span>
      <span class="brand-name">Brisavo</span>
    </header>
    <div class="label__band">
      <h2 class="label__title label__title--wide">Nordische<br>Fichte</h2>
      <p class="label__tagline">Auszeit in der Flasche</p>
    </div>
    <div class="label__art label__art--fichte" role="img" aria-label="Gezeichnete Fichtenwald-Illustration"></div>
  </section>

  <section class="label label--menthol">
    <header class="label__brand">
      <span class="brand-mark"></span>
      <span class="brand-name">Brisavo</span>
    </header>
    <div class="label__band">
      <h2 class="label__title">Menthol<br>Kristalle</h2>
      <p class="label__tagline">Auszeit in der Flasche</p>
    </div>
    <div class="label__art label__art--menthol" role="img" aria-label="Gezeichnete Minzblätter-Illustration"></div>
  </section>

  <section class="label label--granat">
    <header class="label__brand">
      <span class="brand-mark"></span>
      <span class="brand-name">Brisavo</span>
    </header>
    <div class="label__band">
      <h2 class="label__title">Granat<br>Apfel</h2>
      <p class="label__tagline">Auszeit in der Flasche</p>
    </div>
    <div class="label__art label__art--granat" role="img" aria-label="Gezeichnete Granatapfel-Illustration"></div>
  </section>

</main>
</body>
</html>
```